Contractor Business Card Design

Looking to have a card made that has a bold description of (KITCHENS, BASEMENTS, BATHROOMS)

Definition and layers a plus

Contact info is;

Mark T. Ellery
Alder Bend, MN 55990
Cell: 612-555-0147
website: www.cobaltfinishworks.example
Email: cobaltfinishworksmn@mailbox.example

colors: red, black, gray, white

Contact Information for Business Card

Contact info is;

Mark T. Ellery
Alder Bend, MN 55990
Cell: 612-555-0147

Colors
ec1f27

Requirements
Must have
• Looking for layers and definition
Nice to have
• Cards are planned to be printed on plastic cards

```html
<!DOCTYPE html>
<html lang="en">
<head>
<meta charset="utf-8">
<title>Cobalt Finishworks – Business Card</title>
<link rel="stylesheet" href="https://fonts.googleapis.com/css2?family=Montserrat:wght@400;500;600;800&display=swap">
<style>
  :root {
    --brand-red: #c8161e;
    --brand-red-deep: #a3141a;
    --ink-black: #0d0d0d;
    --ink-gray: #333336;
    --text-gray: #3c3c40;
    --card-white: #f1f2f4;
    --backdrop: #d8dce1;
  }
  * { box-sizing: border-box; margin: 0; padding: 0; }
  html, body {
    width: 1200px;
    height: 900px;
    overflow: hidden;
    background: var(--backdrop);
    font-family: "Montserrat", Arial, sans-serif;
  }
  .business-card {
    position: absolute;
    left: 100px;
    top: 165px;
    width: 1000px;
    height: 570px;
    background: var(--card-white);
    overflow: hidden;
    box-shadow: 0 10px 30px rgba(0, 0, 0, 0.12);
  }
  .card-swoosh {
    position: absolute;
    left: 0;
    top: 0;
    width: 1000px;
    height: 570px;
  }
  .brand-mark {
    position: absolute;
    left: 60px;
    top: 125px;
    width: 380px;
    text-align: center;
  }
  .brand-ring {
    display: block;
    margin: 0 auto 30px;
  }
  .brand-name {
    color: var(--ink-gray);
    font-weight: 800;
    font-size: 34px;
    line-height: 44px;
    letter-spacing: 2px;
    text-transform: uppercase;
  }
  .column-divider {
    position: absolute;
    left: 444px;
    top: 125px;
    width: 2px;
    height: 320px;
    background: var(--brand-red);
  }
  .contact-block {
    position: absolute;
    left: 478px;
    top: 136px;
    width: 470px;
  }
  .person-name {
    color: var(--brand-red);
    font-weight: 600;
    font-size: 36px;
    line-height: 42px;
  }
  .person-role {
    color: var(--text-gray);
    font-weight: 400;
    font-size: 21px;
    margin-top: 8px;
  }
  .person-address {
    color: var(--text-gray);
    font-weight: 400;
    font-size: 25px;
    margin-top: 40px;
  }
  .contact-list {
    list-style: none;
    margin-top: 22px;
  }
  .contact-item {
    display: flex;
    align-items: center;
    gap: 20px;
    height: 40px;
    color: var(--text-gray);
    font-size: 22px;
    font-weight: 400;
    white-space: nowrap;
  }
  .contact-item--email {
    font-size: 19px;
  }
  .contact-icon {
    width: 26px;
    height: 26px;
    flex: none;
  }
</style>
</head>
<body>
  <main class="business-card">
    <svg class="card-swoosh" viewBox="0 0 1000 570" aria-hidden="true">
      <defs>
        <linearGradient id="redWave" x1="0" y1="0" x2="1" y2="0">
          <stop offset="0" stop-color="#b8252b"/>
          <stop offset="0.6" stop-color="#c8161e"/>
          <stop offset="1" stop-color="#a3141a"/>
        </linearGradient>
        <linearGradient id="blackWave" x1="0" y1="0" x2="1" y2="0">
          <stop offset="0" stop-color="#0d0d0d" stop-opacity="0"/>
          <stop offset="0.4" stop-color="#0d0d0d"/>
          <stop offset="1" stop-color="#0d0d0d"/>
        </linearGradient>
      </defs>
      <path d="M0,570 V538 C220,520 400,555 560,556 C760,550 900,470 1000,427 V570 Z" fill="url(#redWave)"/>
      <path d="M300,528 C450,552 560,566 680,552 C820,532 920,440 1000,365 V412 C900,482 780,560 620,568 C480,574 400,548 300,528 Z" fill="url(#blackWave)"/>
    </svg>

    <div class="brand-mark">
      <svg class="brand-ring" width="184" height="184" viewBox="0 0 184 184" aria-hidden="true">
        <circle cx="92" cy="92" r="88" fill="none" stroke="var(--ink-gray)" stroke-width="5"/>
      </svg>
      <p class="brand-name">Cobalt<br>Finishworks</p>
    </div>

    <div class="column-divider"></div>

    <section class="contact-block">
      <h1 class="person-name">Mark T. Ellery</h1>
      <p class="person-role">Director</p>
      <p class="person-address">Alder Bend, MN 55990</p>
      <ul class="contact-list">
        <li class="contact-item">
          <svg class="contact-icon" viewBox="0 0 24 24" aria-hidden="true">
            <path d="M6.6 10.8a15.1 15.1 0 0 0 6.6 6.6l2.2-2.2a1 1 0 0 1 1-.25 11.4 11.4 0 0 0 3.6.57 1 1 0 0 1 1 1V20a1 1 0 0 1-1 1A17 17 0 0 1 3 4a1 1 0 0 1 1-1h3.5a1 1 0 0 1 1 1c0 1.25.2 2.450.57 3.57a1 1 0 0 1-.25 1z" fill="var(--brand-red)"/>
          </svg>
          612-555-0147
        </li>
        <li class="contact-item contact-item--email">
          <svg class="contact-icon" viewBox="0 0 24 24" aria-hidden="true">
            <rect x="2" y="5" width="20" height="14" fill="var(--brand-red)"/>
            <path d="M2 5l10 8 10-8M2 19l7-7M22 19l-7-7" fill="none" stroke="var(--card-white)" stroke-width="1.6"/>
          </svg>
          cobaltfinishworksmn@mailbox.example
        </li>
        <li class="contact-item">
          <svg class="contact-icon" viewBox="0 0 24 24" aria-hidden="true">
            <circle cx="12" cy="12" r="10" fill="var(--brand-red)"/>
            <path d="M2 12h20M12 2c3 3 3 17 0 20M12 2c-3 3-3 17 0 20" fill="none" stroke="var(--card-white)" stroke-width="1.4"/>
          </svg>
          www.cobaltfinishworks.example
        </li>
      </ul>
    </section>
  </main>
</body>
</html>
```